Coffee bag product stickers

We currently have 4 blends of coffee (http://www.velmarobeans.com.au/ourcoffee,html) and would like to create a simple design that will be printed on clear/transparent product stickers to be placed on the front of the bags. The bags will be either black or brown so the design will need to work on both.
The design should have a consistent theme across the 4 blends with subtle differences in design or colour used to differentiate between them.
The labels we are looking at are rectangular clear poly synthetic labels, 102 x 76 mm
Information that should be incorporated in the designs is:
- our web site addresses ( www.velmarobeans.com.au )
- Name of the blend
- our logo (please see uploaded files)
Updates
Hi,
The original dimension of 100mm x 100mm have had to be altered to now be 102 mm x 76 mm. Designs do not need to fill this space completely as they will be printed on clear stickers allowing the colour of the bag to show through, however designs should also not be too small.
Many thanks.
FYI - The labels will be printed on clear label stock so the design does not need to fill the whole area and can use the colour of the bag (black - possibly brown on organic) to show through.
The idea is for it to be a sticker we place on the bag in order but for it not to look like a sticker if that make sense. It should almost be like a decal.
Thanks.
Reason: We have seen some excellent ideas and design approaches that never occurred to us while still managing to meet the brief and this is really pleasing. This has prompted us to extend the deadline to encourage more ideas for us to consider and allow us to extend our thinking even further.
Also, we felt completing the project directly after a weekend to be less than ideal.
Also, project is now a committed payment project.
Keep the ideas coming!!
Thanks,
Tobias

```html
<!DOCTYPE html>
<html lang="en">
<head>
<meta charset="utf-8">
<title>Velmaro Beans – Blend Stickers</title>
<link rel="stylesheet" href="https://fonts.googleapis.com/css2?family=Cinzel:wght@400;600&family=Open+Sans:wght@600&display=swap">
<style>
  :root {
    --page: #ffffff;
    --label-bg: #3b1e0f;
    --tan: #d3ad84;
    --tan-light: #e6cdb0;
    --bean-dark: #5a2e14;
    --bean-mid: #9a5a30;
    --premium: #d9a21c;
    --blaze: #e2472a;
    --rumba: #d89a80;
    --organic: #92c63c;
  }
  html, body {
    margin: 0;
    width: 1200px;
    height: 898px;
    overflow: hidden;
    background: var(--page);
  }
  .sheet {
    position: relative;
    width: 1200px;
    height: 898px;
  }
  .sticker {
    position: absolute;
    width: 509px;
    height: 378px;
    background: var(--label-bg);
    overflow: hidden;
  }
  .sticker--premium { left: 83px;  top: 64px;  --blend: var(--premium); }
  .sticker--blaze   { left: 612px; top: 64px;  --blend: var(--blaze); }
  .sticker--rumba   { left: 83px;  top: 457px; --blend: var(--rumba); }
  .sticker--organic { left: 612px; top: 457px; --blend: var(--organic); }

  .sticker__rules {
    position: absolute;
    inset: 0;
  }
  .brand {
    position: absolute;
    top: 52px;
    left: 0;
    width: 100%;
    display: flex;
    justify-content: center;
    align-items: center;
    gap: 14px;
  }
  .brand__name {
    font-family: "Cinzel", serif;
    font-weight: 400;
    color: var(--tan);
    text-align: center;
    line-height: 0.98;
    font-size: 48px;
    letter-spacing: 0.5px;
  }
  .brand__mark {
    width: 54px;
    height: 54px;
    border-radius: 50%;
    background: var(--tan);
  }
  .blend {
    position: absolute;
    top: 176px;
    left: 0;
    width: 100%;
    display: flex;
    align-items: center;
    gap: 12px;
  }
  .blend::before, .blend::after {
    content: "";
    flex: 1;
    height: 3px;
    background: var(--blend);
  }
  .blend__name {
    font-family: "Cinzel", serif;
    font-weight: 400;
    font-size: 30px;
    line-height: 1;
    color: var(--blend);
    white-space: nowrap;
  }
  .beans {
    position: absolute;
    left: 196px;
    top: 224px;
    width: 117px;
    height: 84px;
    border-radius: 42px;
    background: radial-gradient(ellipse at 50% 45%, var(--bean-mid), var(--bean-dark) 75%, transparent 76%);
  }
  .site {
    position: absolute;
    top: 354px;
    left: 0;
    width: 100%;
    text-align: center;
    font-family: "Open Sans", sans-serif;
    font-weight: 600;
    font-size: 14px;
    line-height: 1;
    color: var(--tan-light);
  }
</style>
</head>
<body>
<main class="sheet">

  <section class="sticker sticker--premium">
    <svg class="sticker__rules" width="509" height="378" viewBox="0 0 509 378" aria-hidden="true">
      <rect x="0" y="6" width="509" height="3" fill="#e6cdb0"/>
      <rect x="0" y="15" width="509" height="6" fill="#d3ad84"/>
      <rect x="0" y="332" width="240" height="5" fill="#e6cdb0"/>
      <rect x="269" y="332" width="240" height="5" fill="#e6cdb0"/>
      <rect x="0" y="342" width="509" height="3" fill="#d3ad84"/>
      <rect x="236" y="292" width="5" height="45" fill="#e6cdb0"/>
      <rect x="268" y="292" width="5" height="45" fill="#e6cdb0"/>
    </svg>
    <div class="brand"><div class="brand__name">Velmaro<br>Beans</div><div class="brand__mark"></div></div>
    <div class="blend"><span class="blend__name">Velmaro Premium</span></div>
    <div class="beans" role="img" aria-label="Three roasted coffee beans"></div>
    <div class="site">www.velmarobeans.com.au</div>
  </section>

  <section class="sticker sticker--blaze">
    <svg class="sticker__rules" width="509" height="378" viewBox="0 0 509 378" aria-hidden="true">
      <rect x="0" y="6" width="509" height="3" fill="#e6cdb0"/>
      <rect x="0" y="15" width="509" height="6" fill="#d3ad84"/>
      <rect x="0" y="332" width="240" height="5" fill="#e6cdb0"/>
      <rect x="269" y="332" width="240" height="5" fill="#e6cdb0"/>
      <rect x="0" y="342" width="509" height="3" fill="#d3ad84"/>
      <rect x="236" y="292" width="5" height="45" fill="#e6cdb0"/>
      <rect x="268" y="292" width="5" height="45" fill="#e6cdb0"/>
    </svg>
    <div class="brand"><div class="brand__name">Velmaro<br>Beans</div><div class="brand__mark"></div></div>
    <div class="blend"><span class="blend__name">Blaze</span></div>
    <div class="beans" role="img" aria-label="Three roasted coffee beans"></div>
    <div class="site">www.velmarobeans.com.au</div>
  </section>

  <section class="sticker sticker--rumba">
    <svg class="sticker__rules" width="509" height="378" viewBox="0 0 509 378" aria-hidden="true">
      <rect x="0" y="6" width="509" height="3" fill="#e6cdb0"/>
      <rect x="0" y="15" width="509" height="6" fill="#d3ad84"/>
      <rect x="0" y="332" width="240" height="5" fill="#e6cdb0"/>
      <rect x="269" y="332" width="240" height="5" fill="#e6cdb0"/>
      <rect x="0" y="342" width="509" height="3" fill="#d3ad84"/>
      <rect x="236" y="292" width="5" height="45" fill="#e6cdb0"/>
      <rect x="268" y="292" width="5" height="45" fill="#e6cdb0"/>
    </svg>
    <div class="brand"><div class="brand__name">Velmaro<br>Beans</div><div class="brand__mark"></div></div>
    <div class="blend"><span class="blend__name">Rumba</span></div>
    <div class="beans" role="img" aria-label="Three roasted coffee beans"></div>
    <div class="site">www.velmarobeans.com.au</div>
  </section>

  <section class="sticker sticker--organic">
    <svg class="sticker__rules" width="509" height="378" viewBox="0 0 509 378" aria-hidden="true">
      <rect x="0" y="6" width="509" height="3" fill="#e6cdb0"/>
      <rect x="0" y="15" width="509" height="6" fill="#d3ad84"/>
      <rect x="0" y="332" width="240" height="5" fill="#e6cdb0"/>
      <rect x="269" y="332" width="240" height="5" fill="#e6cdb0"/>
      <rect x="0" y="342" width="509" height="3" fill="#d3ad84"/>
      <rect x="236" y="292" width="5" height="45" fill="#e6cdb0"/>
      <rect x="268" y="292" width="5" height="45" fill="#e6cdb0"/>
    </svg>
    <div class="brand"><div class="brand__name">Velmaro<br>Beans</div><div class="brand__mark"></div></div>
    <div class="blend"><span class="blend__name">Ethical Organic</span></div>
    <div class="beans" role="img" aria-label="Three roasted coffee beans"></div>
    <div class="site">www.velmarobeans.com.au</div>
  </section>

</main>
</body>
</html>
```